Website

I have a client that we built a website for about 10 years ago - https://www.quorvelbrightmoss.com.au/

We would like a fresh new design for it that looks more modern. All the elements, info that's on there needs to be the same but the whole design/layout needs to be modernised.

```html
<!DOCTYPE html>
<html lang="en">
<head>
<meta charset="utf-8">
<title>Quorvel Brightmoss – Name Badges</title>
<link href="https://fonts.googleapis.com/css2?family=Roboto:wght@500;700;900&family=Open+Sans:wght@400;600;700&display=swap" rel="stylesheet">
<style>
:root{
  --red:#b8001e;
  --red-dark:#8f0016;
  --ink:#1c1c1c;
  --text:#5f5f5f;
  --grey-bg:#f1f1f1;
  --field:#f4f4f4;
  --line:#dcdcdc;
  --footer:#2d2d2d;
  --white:#ffffff;
}
*{box-sizing:border-box;margin:0;padding:0}
html,body{width:1200px;height:3856px;overflow:hidden}
body{position:relative;background:var(--white);font-family:"Open Sans",Arial,sans-serif;color:var(--ink)}
.abs{position:absolute}
h1,h2{font-family:"Roboto",Arial,sans-serif;font-weight:700;color:var(--ink)}
.rule{position:absolute;height:3px;width:58px;background:var(--red);z-index:2}
.btn{position:absolute;z-index:3;display:flex;align-items:center;justify-content:center;border-radius:26px;color:var(--white);font-family:"Open Sans",Arial,sans-serif;font-weight:700;font-size:15px;background:var(--red)}

/* top bar */
.topbar{left:0;top:0;width:1200px;height:28px;background:var(--red);color:var(--white);font-size:10.5px}
.topbar span{position:absolute;top:7px}
.topbar .soc{position:absolute;top:9px;width:9px;height:9px;background:var(--white);border-radius:2px}

/* header */
.brand{left:145px;top:46px;font-family:"Roboto",Arial,sans-serif;font-weight:700;font-size:17px;line-height:19px;color:var(--red);width:130px}
.field-sm{position:absolute;top:51px;height:36px;border:1px solid var(--line);border-radius:18px;font-size:11px;color:#777;padding:10px 14px}
.field-sm i{font-style:normal;color:var(--red)}
.login{left:751px;top:51px;width:79px;height:36px;font-size:11px}
.phone-dot{left:878px;top:47px;width:41px;height:41px;border-radius:50%;background:var(--red)}
.phone-num{left:934px;top:47px;font-family:"Roboto",Arial,sans-serif;font-weight:500;font-size:18px;color:var(--red)}
.phone-sub{left:934px;top:72px;font-size:10.5px;color:#777}
.nav{left:142px;top:114px;width:914px;display:flex;justify-content:space-between;font-size:14px;color:#222}
.nav .on{color:var(--red)}

/* hero */
.hero{left:0;top:144px;width:1200px;height:546px;background:linear-gradient(90deg,#f3f3f3 0%,#eceeef 55%,#e2e5e8 100%);overflow:hidden}
.hero-photo{left:628px;top:0;width:572px;height:546px;background:linear-gradient(100deg,rgba(226,229,232,0) 0%,#b9c0c8 22%,#5b6675 55%,#2f3946 80%,#6b7684 100%)}
.kicker{left:143px;top:214px;font-weight:700;font-size:15px;color:var(--red)}
.hero-title{position:absolute;left:141px;top:246px;width:620px;font-size:54px;line-height:68px}
.hero-copy{left:143px;top:392px;width:510px;font-size:13.3px;line-height:23px;color:#333}
.dot{position:absolute;left:58px;width:10px;height:10px;border-radius:50%;border:1.5px solid #444}

/* products */
.sec-title{position:absolute;left:0;width:1200px;text-align:center;font-family:"Roboto",Arial,sans-serif;font-weight:700;font-size:38px;z-index:2}
.prod-lift{left:607px;top:832px;width:217px;height:206px;background:var(--white);border-radius:12px;box-shadow:0 6px 22px rgba(0,0,0,.16)}
.prod-img{position:absolute;top:841px;width:200px;height:151px;border-radius:10px}
.prod-label{position:absolute;top:1006px;width:200px;text-align:center;font-size:14px;color:#222}
.arrow-c{position:absolute;width:40px;height:40px;border-radius:50%;display:flex;align-items:center;justify-content:center}

/* about */
.grey{left:0;top:1115px;width:1200px;height:620px;background:var(--grey-bg)}
.about-sub{left:144px;top:1310px;width:420px;color:var(--red);font-size:18px;line-height:29px}
.about-copy{left:144px;top:1378px;width:428px;font-size:13px;line-height:22.5px;color:var(--text);text-align:justify}
.about-copy p+p{margin-top:7px}
.ring{left:646px;top:1225px;width:424px;height:424px;border-radius:50%;border:5px solid var(--red)}
.circle-photo{left:636px;top:1214px;width:424px;height:424px;border-radius:50%;background:radial-gradient(circle at 55% 65%,#c9b8a8 0%,#8d8f96 45%,#4a505a 100%);overflow:hidden}
.circle-photo .t1{position:absolute;top:34px;width:424px;text-align:center;color:var(--white);font-family:"Roboto",Arial,sans-serif;font-weight:700;font-size:17px}
.circle-photo .t2{position:absolute;top:56px;width:424px;text-align:center;color:var(--white);font-family:"Roboto",Arial,sans-serif;font-weight:500;font-size:31px}

/* why */
.why-copy{left:157px;top:1816px;width:886px;text-align:center;font-size:13px;line-height:24px;color:var(--text)}
.feat{position:absolute;font-size:16.5px;color:#222}
.centre-brand{left:460px;top:1985px;width:280px;text-align:center;font-family:"Roboto",Arial,sans-serif;font-weight:900;font-size:31px;line-height:34px;color:var(--red)}

/* testimonials */
.t-card{position:absolute;top:2548px;width:296px;height:163px;background:var(--white);border-radius:8px;padding:18px 22px}
.stars{color:#f2b100;font-size:15px;letter-spacing:2px}
.quote{position:absolute;right:20px;top:14px;font-family:Georgia,serif;font-size:34px;line-height:30px;color:#c9c9c9}
.t-card p{margin-top:12px;font-size:12.4px;line-height:23px;color:#666;text-align:justify}
.avatar{position:absolute;top:2741px;width:55px;height:55px;border-radius:50%;background:radial-gradient(circle,#d9c4b2,#9a8a80);border:2px solid var(--white)}
.who{position:absolute;font-size:14.5px;line-height:23px;color:var(--white);font-weight:600}

/* contact */
.field{position:absolute;height:54px;background:var(--field);border:1px solid #e2e2e2;border-radius:8px;font-size:11.5px;color:#777;padding:19px 22px}
.field i{font-style:normal;color:var(--red)}

/* footer */
.footer{left:0;top:3384px;width:1200px;height:472px}
.f-brand{left:145px;top:3545px;width:200px;font-family:"Roboto",Arial,sans-serif;font-weight:700;font-size:25px;line-height:25px;color:var(--white)}
.f-head{position:absolute;top:3446px;font-size:17px;color:var(--white)}
.f-list{position:absolute;top:3482px;list-style:none;font-size:13.5px;line-height:24px;color:#e8e8e8}
.f-item{position:absolute;left:836px;font-size:13.5px;line-height:24px;color:#e8e8e8}
.f-ico{position:absolute;left:805px;width:20px;height:20px;border-radius:50%;background:var(--red)}
.f-rule{left:144px;top:3740px;width:912px;height:1px;background:#5a5a5a}
.copy{left:0;top:3757px;width:1200px;text-align:center;font-size:13.5px;color:#e8e8e8}
.soc-c{position:absolute;top:3794px;width:27px;height:27px;border-radius:50%;border:1px solid #888}
</style>
</head>
<body>

<!-- top bar -->
<div class="abs topbar">
  <span style="left:688px">✎ Register here</span>
  <span style="left:828px">🛒 Your Cart (30.00)</span>
  <div class="soc" style="left:975px"></div><div class="soc" style="left:988px"></div><div class="soc" style="left:1001px"></div><div class="soc" style="left:1014px"></div><div class="soc" style="left:1027px;border-radius:50%"></div><div class="soc" style="left:1041px"></div>
</div>

<!-- header -->
<div class="abs brand">Quorvel<br>Brightmoss</div>
<div class="field-sm" style="left:368px;width:185px">User Name <i>*</i></div>
<div class="field-sm" style="left:560px;width:184px">Password <i>*</i></div>
<div class="btn login">🔒 LOGIN</div>
<div class="abs phone-dot">
  <svg width="41" height="41" viewBox="0 0 41 41"><path d="M15 13c1-1 2-1 3 0l2 3c.5 1 0 2-.8 2.6l-1 .8c1 2.2 2.6 3.8 4.6 4.8l.8-1c.6-.8 1.6-1.2 2.6-.7l3 2c1 .7 1 2 0 3l-1.4 1.3C24 32 10 18 13.7 14.3z" fill="#fff"/></svg>
</div>
<div class="abs phone-num">1.800.555.0142</div>
<div class="abs phone-sub">Call Us Now</div>
<nav class="abs nav">
  <span class="on">HOME</span><span>PRODUCTS</span><span>PRICE LIST</span><span>INFO</span><span>RE-SELLERS TRADE INFO</span><span>ARTWORK REQUIREMENTS</span><span>PAYMENT</span><span>CONTACT US</span>
</nav>

<!-- hero -->
<section class="abs hero">
  <div class="abs hero-photo" role="img" aria-label="Photo of three smiling business people in suits reviewing a black folder together"></div>
  <svg class="abs" style="left:0;top:440px" width="1200" height="106" viewBox="0 0 1200 106"><path d="M0 26 Q620 150 1200 6 L1200 106 L0 106 Z" fill="#fff"/></svg>
</section>
<div class="abs kicker">Let us Introduce you!</div>
<h1 class="hero-title">Do Your People Need Name Badges Fast?</h1>
<div class="abs hero-copy">At Quorvel Brightmoss we focus on providing our clients badges and name tags at lightning speed and to the highest quality. With no minimum order, free setup and SUPER FAST delivery you've come the right place!</div>
<div class="btn" style="left:144px;top:500px;width:239px;height:51px">Order Your Badges Now</div>
<div class="btn" style="left:392px;top:500px;width:168px;height:51px;background:var(--ink)">Request Quote</div>
<div class="dot" style="top:349px"></div>
<div class="dot" style="top:365px;background:#333"></div>
<div class="dot" style="top:381px"></div>
<div class="dot" style="top:397px"></div>

<!-- products -->
<h2 class="sec-title" style="top:738px">Our Products</h2>
<div class="rule" style="left:571px;top:795px"></div>
<div class="abs prod-lift"></div>
<div class="prod-img" style="left:154px;background:linear-gradient(135deg,#3b3b3b,#d9d5cc 40%,#e8e2d4 70%,#444)" role="img" aria-label="Photo of assorted full colour printed name badges"></div>
<div class="prod-img" style="left:384px;background:radial-gradient(circle at 50% 50%,#c8483b,#3f7d3b 40%,#252525 75%)" role="img" aria-label="Photo of colourful printed button badges"></div>
<div class="prod-img" style="left:616px;background:linear-gradient(180deg,#2b2b2b,#555 50%,#3a3a3a)" role="img" aria-label="Photo of a photo ID card in a clear holder"></div>
<div class="prod-img" style="left:847px;background:linear-gradient(160deg,#2a2a2a,#d8d8d8 45%,#f0f0f0 60%,#2a2a2a)" role="img" aria-label="Photo of printed lanyards with metal clips"></div>
<div class="prod-label" style="left:154px">Full Colour Name Badges</div>
<div class="prod-label" style="left:384px">Button Badges</div>
<div class="prod-label" style="left:616px">Photo ID Cards</div>
<div class="prod-label" style="left:847px">Lanyards</div>
<div class="arrow-c" style="left:95px;top:896px;border:1px solid #999;background:#fff"><svg width="18" height="10"><path d="M17 5H2M6 1L2 5l4 4" stroke="#333" stroke-width="1.4" fill="none"/></svg></div>
<div class="arrow-c" style="left:1071px;top:896px;background:#4a4a4a"><svg width="18" height="10"><path d="M1 5h15M12 1l4 4-4 4" stroke="#fff" stroke-width="1.4" fill="none"/></svg></div>

<!-- about -->
<div class="abs grey"></div>
<svg class="abs" style="left:0;top:1114px" width="1200" height="80" viewBox="0 0 1200 80"><path d="M0 0 Q600 140 1200 0 Z" fill="#fff"/></svg>
<svg class="abs" style="left:0;top:1675px" width="1200" height="62" viewBox="0 0 1200 62"><path d="M0 62 Q600 -50 1200 62 Z" fill="#fff"/></svg>
<div class="btn" style="left:528px;top:1082px;width:143px;height:42px;font-size:14px">Learn More</div>
<h2 class="abs" style="left:143px;top:1218px;font-size:38px">Name Tags Australia</h2>
<div class="rule" style="left:144px;top:1274px"></div>
<div class="abs about-sub">The best custom name badges for companies and individuals across Australia.</div>
<div class="abs about-copy">
  <p>Do you need Name Badges for your company or an upcoming event? At Quorvel Brightmoss we specialise in producing a range of identity name tags and ID products.</p>
  <p>Tailor your name tags to suit your exact requirements with a choice of sizes, colours, fittings and finishes. Quorvel Brightmoss offers a full range of reusable name badges so you can get the maximum usage from your quality name tags.</p>
</div>
<div class="btn" style="left:144px;top:1580px;width:136px;height:43px;font-size:14px">Read More</div>
<div class="abs ring"></div>
<div class="abs circle-photo" role="img" aria-label="Photo of professionals mingling and shaking hands at a networking event">
  <div class="t1">Have an event coming up?</div>
  <div class="t2">Let us introduce you</div>
</div>

<!-- why choose us -->
<h2 class="sec-title" style="top:1735px">Why Choose Us?</h2>
<div class="abs why-copy">Quorvel Brightmoss is one of Australia's most trusted names for ID products and services. Here's why our clients are continually satisfied with our name badges Australia company:</div>
<svg class="abs" style="left:380px;top:1890px" width="440" height="380" viewBox="0 0 440 380">
  <defs><radialGradient id="glow"><stop offset="0" stop-color="#f2f2f2"/><stop offset="1" stop-color="#fff"/></radialGradient></defs>
  <circle cx="219" cy="145" r="140" fill="url(#glow)"/>
  <path d="M60 26 A199 199 0 1 0 378 26" fill="none" stroke="var(--red)" stroke-width="6" stroke-linecap="round"/>
</svg>
<div class="abs centre-brand">Quorvel<br>Brightmoss</div>
<svg class="abs" style="left:0;top:0;pointer-events:none" width="1200" height="2300" viewBox="0 0 1200 2300">
  <g fill="var(--red)" stroke="#fff" stroke-width="5">
    <circle cx="401" cy="1997" r="46"/><circle cx="800" cy="1997" r="46"/>
    <circle cx="440" cy="2150" r="46"/><circle cx="763" cy="2150" r="46"/>
    <circle cx="600" cy="2237" r="46"/>
  </g>
  <g fill="none" stroke="#fff" stroke-width="2.2" stroke-linecap="round" stroke-linejoin="round">
    <circle cx="397" cy="1997" r="11"/><circle cx="397" cy="1997" r="4"/><path d="M408 2012l14-22 4 3-14 22-5 2z"/>
    <rect x="787" y="1992" width="20" height="16"/><path d="M807 1998h8l4 5v5h-12M791 2012a3 3 0 1 0 0 1M813 2012a3 3 0 1 0 0 1"/>
    <circle cx="440" cy="2144" r="13"/><path d="M433 2144l5 5 10-10M432 2155l-5 12 6-2 3 5 4-10M448 2155l5 12-6-2-3 5-4-10"/>
    <rect x="749" y="2136" width="26" height="26"/><path d="M754 2157l16-16M754 2157v-6M754 2157h6"/>
    <rect x="588" y="2228" width="24" height="20"/><path d="M588 2236h24M598 2228v8M603 2220l-3 8"/>
  </g>
</svg>
<div class="feat" style="left:153px;top:1985px">In-depth customisation</div>
<div class="feat" style="left:865px;top:1986px">Super-fast delivery</div>
<div class="feat" style="left:202px;top:2139px">High-quality materials</div>
<div class="feat" style="left:831px;top:2142px">Free design setup</div>
<div class="feat" style="left:0;top:2308px;width:1200px;text-align:center">Free postage for badge orders over $400</div>

<!-- testimonials -->
<svg class="abs" style="left:0;top:2334px" width="1200" height="600" viewBox="0 0 1200 600">
  <path d="M0 0 Q600 130 1200 0 L1200 598 Q600 510 0 598 Z" fill="var(--red)"/>
  <path d="M0 300 Q300 200 650 330 T1200 290" fill="none" stroke="#c4102c" stroke-width="40" opacity=".35"/>
</svg>
<h2 class="sec-title" style="top:2460px;color:#fff">Customer Testimonials</h2>
<div class="rule" style="left:571px;top:2518px;background:#fff"></div>
<svg class="abs" style="left:90px;top:2617px" width="20" height="26"><path d="M15 2L4 13l11 11" stroke="#fff" stroke-width="2.5" fill="none"/></svg>
<svg class="abs" style="left:1092px;top:2617px" width="20" height="26"><path d="M5 2l11 11L5 24" stroke="#fff" stroke-width="2.5" fill="none"/></svg>

<div class="t-card" style="left:142px"><div class="stars">★★★★★</div><span class="quote">❝</span>
  <p>I thought I'd send a quick note to say thank you for the great service, I was really happy with the customer service you provided and the prompt delivery...</p></div>
<div class="t-card" style="left:451px"><div class="stars">★★★★★</div><span class="quote">❝</span>
  <p>Badges arrived yesterday and we are absolutely thrilled with them. Many thanks for your attention to detail, courtesy in your emails and blinding speed in filling...</p></div>
<div class="t-card" style="left:759px"><div class="stars">★★★★★</div><span class="quote">❝</span>
  <p>I also wanted to sincerely thank you for providing such quality to DDS. We have had several rounds of trouble getting these badges right from other....</p></div>
<div class="avatar" style="left:144px" role="img" aria-label="Customer portrait"></div>
<div class="avatar" style="left:452px" role="img" aria-label="Customer portrait"></div>
<div class="avatar" style="left:761px" role="img" aria-label="Customer portrait"></div>
<div class="who" style="left:214px;top:2757px">Loretta - Fernvale Living Group</div>
<div class="who" style="left:523px;top:2745px;width:230px">Beatrix - Lead Hatter, Marlow Crimson Hatters, Ashby</div>
<div class="who" style="left:831px;top:2745px;width:220px">Corinne, Dunmore Drilling Supplies, Halbrook</div>

<!-- contact -->
<h2 class="sec-title" style="top:2934px">Contact Us</h2>
<div class="rule" style="left:571px;top:2992px"></div>
<div class="field" style="left:191px;top:3041px;width:392px">👤 Full Name <i>*</i></div>
<div class="field" style="left:191px;top:3107px;width:392px">📞 Phone Number <i>*</i></div>
<div class="field" style="left:191px;top:3173px;width:392px">✉ Email Address <i>*</i></div>
<div class="field" style="left:616px;top:3041px;width:391px;height:186px">💬 Message <i>*</i></div>
<div class="btn" style="left:520px;top:3266px;width:159px;height:42px;font-size:14px">SUBMIT NOW</div>

<!-- footer -->
<svg class="abs footer" width="1200" height="472" viewBox="0 0 1200 472"><path d="M0 72 Q600 -40 1200 72 L1200 472 L0 472 Z" fill="var(--footer)"/></svg>
<div class="abs f-brand">Quorvel<br>Brightmoss</div>
<div class="f-head" style="left:401px">Quick Links</div>
<ul class="f-list" style="left:403px"><li>Home</li><li>Products</li><li>Price List</li><li>Re-sellers</li><li>Trade Info</li><li>Faqs</li><li>Artwork</li><li>Requirements</li><li>Payment</li><li>Contact Us</li></ul>
<div class="f-head" style="left:561px">Other Links</div>
<ul class="f-list" style="left:563px"><li>Nurse Name Badges</li><li>Identification Name Badges</li><li>Magnetic Name Tags</li><li>Plastic Name Badges</li><li>Site Map</li></ul>
<div class="f-head" style="left:802px">Contact Us</div>
<div class="f-ico" style="top:3489px"></div><div class="f-item" style="left:840px;top:3487px">1300 555 014</div>
<div class="f-ico" style="top:3530px"></div><div class="f-item" style="top:3528px">info@quorvelbrightmoss.com.au</div>
<div class="f-ico" style="top:3569px"></div><div class="f-item" style="top:3567px;width:230px">PO Box 40871, Harlow Heights QLD 4399</div>
<div class="f-ico" style="top:3622px"></div><div class="f-item" style="top:3620px">03 5550 2719</div>
<div class="abs f-rule"></div>
<div class="abs copy">© 2026 Copyright - Quorvel Brightmoss. All Rights Reserved.</div>
<div class="soc-c" style="left:513px"></div>
<div class="soc-c" style="left:550px;background:var(--red);border-color:var(--red)"></div>
<div class="soc-c" style="left:586px"></div>
<div class="soc-c" style="left:623px"></div>
<div class="soc-c" style="left:659px"></div>

</body>
</html>
```